Pale Fern The Vapor Parlor needs a room spray label

We are a company that is dedicated to the aromatization services for our customers, we have just created an aromatic product that is a Room Spray for the customer to spray it in their spaces and we are looking for the most sophisticated and luxurious label in the market, help us? Thanks a lot!

Target Market(s)

That the label represents an elegant and exclusive aroma

Font styles to use
Serif

Colors

Designer to choose colors to be used in the design.

Requirements
Must have
• Elegance, fine, luxury and cleanliness
Nice to have
• The fonts I like are those of the logo, they are called "Cinzel_Regular" and "MrEaveXL"
They can propose in color but I think it looks better in black and gray or white, however I would like to see something in color

```html
<!DOCTYPE html>
<html lang="en">
<head>
<meta charset="utf-8">
<title>Pale Fern — Room Spray Label</title>
<link href="https://fonts.googleapis.com/css2?family=Cinzel:wght@400&family=Crimson+Pro:wght@400&display=swap" rel="stylesheet">
<style>
  :root {
    --paper: #ffffff;
    --ink: #111111;
    --brand-grey: #5a5a5a;
    --rule-grey: #8a8a8a;
    --mark-grey: #6b6b6b;
    --scene-light: #d9d9d9;
    --scene-dark: #8f8f8f;
  }
  html, body {
    margin: 0;
    padding: 0;
    width: 1200px;
    height: 1080px;
    overflow: hidden;
    background: var(--paper);
  }
  .canvas {
    position: relative;
    width: 1200px;
    height: 1080px;
    background: var(--paper);
    font-family: "Crimson Pro", Georgia, serif;
    color: var(--ink);
  }
  .bottle-view {
    position: absolute;
    left: 0;
    top: 30px;
    width: 385px;
    height: 1022px;
    background: linear-gradient(180deg, var(--scene-light) 0%, #c4c4c4 55%, var(--scene-dark) 100%);
  }
  .label-rule {
    position: absolute;
    left: 460px;
    width: 666px;
    height: 30px;
  }
  .label-rule--top { top: 96px; }
  .label-rule--bottom { top: 954px; }

  .brand-mark {
    position: absolute;
    left: 548px;
    top: 210px;
    width: 160px;
    height: 160px;
    border: 2px solid var(--mark-grey);
    border-radius: 50%;
    box-sizing: border-box;
  }
  .brand-name {
    position: absolute;
    left: 440px;
    width: 376px;
    text-align: center;
    font-family: "Cinzel", Georgia, serif;
    font-weight: 400;
    color: var(--brand-grey);
    margin: 0;
    line-height: 1;
  }
  .brand-name__main { top: 420px; font-size: 44px; }
  .brand-name__sub { top: 466px; font-size: 19px; letter-spacing: 5px; }

  .product-title {
    position: absolute;
    left: 500px;
    top: 592px;
    width: 250px;
    margin: 0;
    font-weight: 400;
    font-size: 60px;
    line-height: 72px;
  }
  .product-title span { display: block; }
  .product-title .line-2 { padding-left: 14px; }
  .product-scent {
    position: absolute;
    left: 529px;
    top: 768px;
    margin: 0;
    font-size: 20px;
    letter-spacing: 0.3px;
  }
  .product-volume {
    position: absolute;
    left: 546px;
    top: 920px;
    margin: 0;
    font-size: 19px;
  }

  .brief-tag {
    position: absolute;
    left: 846px;
    top: 175px;
    display: flex;
    align-items: center;
    gap: 16px;
  }
  .brief-tag__mark {
    width: 44px;
    height: 44px;
    border: 1.5px solid var(--mark-grey);
    border-radius: 50%;
    box-sizing: border-box;
  }
  .brief-tag__text {
    font-family: "Cinzel", Georgia, serif;
    font-size: 13px;
    line-height: 19px;
    color: var(--ink);
    margin: 0;
  }

  .info-block {
    position: absolute;
    left: 853px;
    width: 300px;
  }
  .info-block h2 {
    font-family: "Cinzel", Georgia, serif;
    font-weight: 400;
    font-size: 20px;
    margin: 0 0 6px 0;
    letter-spacing: 0.5px;
  }
  .info-block p {
    margin: 0 0 0 12px;
    font-size: 17px;
    line-height: 22px;
  }
  .info-block p + p { margin-top: 22px; }
  .info-block--use { top: 267px; }
  .info-block--ingredients { top: 472px; }
  .info-block--cautions { top: 747px; }
</style>
</head>
<body>
<div class="canvas">
  <div class="bottle-view" role="img" aria-label="Photo of a hand holding the clear spray bottle with the label applied, with drawn height and 4.5 cm width measurements"></div>

  <svg class="label-rule label-rule--top" viewBox="0 0 666 30" aria-hidden="true">
    <line x1="0" y1="6" x2="666" y2="6" stroke="#8a8a8a" stroke-width="2"/>
    <line x1="0" y1="12" x2="666" y2="12" stroke="#8a8a8a" stroke-width="1"/>
    <rect x="300" y="10" width="66" height="18" fill="#8a8a8a" role="img" aria-label="Centre ornament"/>
  </svg>

  <div class="brand-mark"></div>
  <p class="brand-name brand-name__main">PALE FERN</p>
  <p class="brand-name brand-name__sub">THE VAPOR PARLOR</p>

  <h1 class="product-title"><span class="line-1">ROOM</span><span class="line-2">SPRAY</span></h1>
  <p class="product-scent">AROMA LAVENDER</p>
  <p class="product-volume">100mL / 3.4 fl oz</p>

  <div class="brief-tag">
    <div class="brief-tag__mark"></div>
    <p class="brief-tag__text">NECESITA UNA ETIQUETA<br>PARA ROOM SPRAY</p>
  </div>

  <section class="info-block info-block--use">
    <h2>HOW TO USE</h2>
    <p>Lorem ipsum dolor sit amet, con-<br>sectetuer adipiscing elit, sed diam<br>nonummy nibh euismod tinci-<br>dunt ut laoreet dolore<br>magna aliquam erat volutpat.<br>Ut wisi enim ad minim veniam,<br>quis nostrud exerci tation</p>
  </section>

  <section class="info-block info-block--ingredients">
    <h2>INGREDIENTS</h2>
    <p>Water (Aqua), Alcohol Denat.,<br>PEG-40 Hydrogenated Castor<br>Oil, Fragrance (Parfum),<br>Polysorbate 80, Citronellol</p>
    <p>This ingredient list is subject<br>to change; clients should<br>refer to the product packaging<br>for the most up-to-date<br>ingredient list.</p>
  </section>

  <section class="info-block info-block--cautions">
    <h2>CAUTIONS</h2>
    <p>Lavender, Tabacco, Strawberry<br>Jasmine And Other.</p>
  </section>

  <svg class="label-rule label-rule--bottom" viewBox="0 0 666 30" aria-hidden="true">
    <rect x="300" y="2" width="66" height="18" fill="#8a8a8a" role="img" aria-label="Centre ornament"/>
    <line x1="0" y1="18" x2="666" y2="18" stroke="#8a8a8a" stroke-width="1"/>
    <line x1="0" y1="24" x2="666" y2="24" stroke="#8a8a8a" stroke-width="2"/>
  </svg>
</div>
</body>
</html>
```